Hong Kong residential leasing and sales company needs a website design

Hong Kong has many competitive real estate agents. The majority of us have the same listings so, besides the team and experience, a website is what makes us stand out. A first impression. We need our website to be user friendly, informative and to have a wow factor. Most sites are generic so whilst we are close to accepting that maybe that's the only formula which works....we would like to see if we're missing something! Our clients are a mix of International users of all ages but probably ultimately 35+.. We have a logo (attached) which we would like to keep - designed by brushforum. Flexible with colours except red.
examples of our competitors are:
http://www.marlowvesthomes.example
http://www.tuvix.example/home
http://www.premierdwellingsgr.example
http://www.nestora-estates.example
http://www.fieldmark-ardley.example
We were thinking of having the following in a menu bar with drop downs for most...some more than others. Home / For Sale / For Rent / Property 101 / About us / Contact Us ..
Look forward to seeing your ideas. Thanks in advance.

```html
<!DOCTYPE html>
<html lang="en">
<head>
<meta charset="utf-8">
<title>Lanternway Homes</title>
<link rel="stylesheet" href="https://fonts.googleapis.com/css2?family=Cinzel:wght@400;600&family=Open+Sans:ital,wght@0,400;0,600;0,700;1,400;1,600;1,700&display=swap">
<style>
:root{
  --purple:#6b3b93;
  --purple-deep:#5a2d82;
  --purple-nav:#8246a6;
  --ink:#222;
  --grey-text:#555;
  --nav-bg:#262626;
  --body-bg:#f0f0f0;
  --footer-bg:#2a1b37;
  --white:#fff;
}
*{box-sizing:border-box;margin:0;padding:0}
html,body{width:1055px;height:1200px;overflow:hidden}
body{position:relative;background:var(--body-bg);font-family:"Open Sans",sans-serif;color:var(--ink)}
.abs{position:absolute}
.header{left:0;top:0;width:1055px;height:106px;background:var(--white)}
.brand{left:183px;top:38px;display:flex;align-items:center;gap:8px;font-family:"Cinzel",serif;font-weight:600;font-size:20px;color:var(--purple-deep)}
.brand-dot{width:14px;height:14px;background:var(--purple-deep)}
.inquiry{left:545px;top:64px;font-size:19px;font-style:italic;color:var(--purple-deep);letter-spacing:.5px}
.language{left:772px;top:66px;width:100px;height:22px;border:1px solid #ccc;font-size:11px;color:#777;display:flex;align-items:center;padding-left:7px;gap:6px}
.flag{width:13px;height:9px;background:linear-gradient(#3b5aa8 0 45%,#d33 45%)}
.lang-arrow{margin-left:auto;margin-right:6px;width:8px;height:8px;border-radius:50%;background:#ccc}
.nav{left:0;top:106px;width:1055px;height:46px;background:linear-gradient(#333,#1e1e1e);border-bottom:3px solid var(--purple-nav)}
.nav-item{position:absolute;top:0;height:46px;line-height:46px;font-family:"Cinzel",serif;font-size:14px;color:var(--white);letter-spacing:.5px;white-space:nowrap}
.nav-item.active{background:var(--purple-nav);text-align:center}
.caret{display:inline-block;width:7px;height:7px;border-radius:50%;background:var(--white);margin-left:6px;vertical-align:1px}
.social{left:825px;top:121px;display:flex;gap:8px;align-items:center}
.social-dot{width:10px;height:10px;border-radius:50%;background:var(--white)}
.hero{left:0;top:155px;width:1055px;height:473px;background:linear-gradient(100deg,#b5a58a 0%,#8c7660 30%,#cfc5b3 55%,#7b5d43 80%,#a38b70 100%)}
.caption-band{left:0;top:316px;width:1055px;height:59px;background:rgba(255,255,255,.35)}
.caption{left:0;width:1055px;text-align:center;color:rgba(255,255,255,.7);font-size:13px}
.dropdown{left:242px;top:152px;width:481px;height:209px;background:rgba(255,255,255,.94)}
.menu-col{top:24px;width:100px;list-style:none}
.menu-col li{font-size:10px;height:23.7px;line-height:23px;border-bottom:1px solid #e3e3e3;padding-left:13px;position:relative;color:#222;white-space:nowrap}
.menu-col li::before{content:"›";position:absolute;left:3px;color:#666}
.dropdown-photo{left:286px;top:47px;width:169px;height:127px;background:linear-gradient(#6f93c9 0 45%,#e7e7e2 45% 75%,#5d8a3a 75%)}
.dots{left:508px;top:390px;display:flex;gap:3px}
.dots span{width:8px;height:8px;border-radius:50%;background:#999}
.dots span:first-child{background:var(--purple-nav);border:2px solid #fff}
.hide-label{left:0;width:1055px;top:440px;text-align:center;font-size:10px;color:#eee}
.hide-btn{left:515px;top:458px;width:24px;height:24px;border-radius:50%;background:#fff}
.search-panel{left:370px;top:471px;width:315px;height:157px;background:rgba(30,30,30,.55)}
.tab{top:35px;height:26px;width:73px;font-weight:700;font-size:13px;text-align:center;line-height:26px}
.tab.rent{left:84px;background:var(--purple-deep);color:#fff}
.tab.buy{left:160px;background:#ccc;color:#888}
.keyword{left:26px;top:68px;width:264px;height:30px;background:#fff;text-align:center;line-height:30px;font-size:13px;font-style:italic;color:#999}
.search-btn{left:70px;top:105px;width:175px;height:33px;border:1px solid #fff;color:#fff;font-weight:700;font-size:12px;display:flex;align-items:center;justify-content:center;gap:5px}
.welcome{left:0;width:1055px;top:666px;text-align:center;font-family:"Cinzel",serif;font-weight:600;font-size:28px;color:var(--purple-deep);letter-spacing:.5px}
.intro{left:232px;top:708px;width:591px;text-align:center;font-size:11.3px;line-height:16px;color:#222}
.featured-label{left:449px;top:786px;width:156px;height:22px;border:1px solid #aaa;text-align:center;line-height:20px;font-size:10px;color:#666}
.card{top:826px;width:166px;height:138px}
.card-photo{width:166px;height:121px}
.ref{position:absolute;left:0;top:121px;height:17px;width:95px;background:#666;color:#fff;font-size:10px;line-height:17px;padding-left:9px;clip-path:polygon(0 0,100% 0,82% 100%,0 100%)}
.ref.dark{background:#111}
.card-over{position:absolute;left:0;top:0;width:166px;height:121px;background:rgba(0,0,0,.35);color:#fff;text-align:center}
.card-over h3{font-weight:400;font-size:14px;margin-top:34px}
.card-over p{font-size:11px}
.plus{width:22px;height:22px;border-radius:50%;background:var(--purple-nav);margin:6px auto 0;line-height:22px;font-size:14px}
.see-all{left:183px;top:987px;font-size:11px;color:#555;border-bottom:1px dashed #888;padding-bottom:1px}
.footer{left:0;top:1053px;width:1055px;height:147px;background:var(--footer-bg);border-top:2px solid #ddd;color:#fff;text-align:center}
.footer-links{margin-top:30px;font-size:10px;display:flex;gap:14px;justify-content:center}
.footer-call{margin-top:10px;font-size:13px;font-weight:700;font-style:italic;display:flex;gap:8px;justify-content:center;align-items:center}
.footer-copy{margin-top:8px;font-size:9.5px;font-style:italic}
</style>
</head>
<body>
<header class="abs header">
  <div class="abs brand"><span class="brand-dot"></span>Lanternway Homes</div>
  <div class="abs inquiry">INQUIRY +842 5550 1987</div>
  <div class="abs language"><span class="flag"></span>Language<span class="lang-arrow"></span></div>
</header>

<section class="abs hero" role="img" aria-label="Bright living room interior with sofas, coffee table and city windows"></section>
<div class="abs caption-band"></div>
<div class="abs caption" style="top:327px">Lorem Ipsum Hong Kong Property Title</div>
<div class="abs caption" style="top:349px">Hongkong Location, Size...</div>
<div class="abs dots"><span></span><span></span><span></span><span></span><span></span></div>

<nav class="abs nav">
  <span class="nav-item" style="left:182px">HOME</span>
  <span class="nav-item active" style="left:242px;width:110px">FOR SALE<span class="caret"></span></span>
  <span class="nav-item" style="left:370px">FOR RENT<span class="caret"></span></span>
  <span class="nav-item" style="left:487px">PROPERTY 101</span>
  <span class="nav-item" style="left:617px">ABOUT US</span>
  <span class="nav-item" style="left:720px">CONTACT US</span>
</nav>
<div class="abs social">
  <span class="social-dot"></span><span class="social-dot"></span>
  <svg width="15" height="11" viewBox="0 0 15 11"><rect x=".5" y=".5" width="14" height="10" fill="none" stroke="#fff"/><path d="M.5 .5 7.5 6 14.5 .5" fill="none" stroke="#fff"/></svg>
</div>

<div class="abs dropdown">
  <ul class="abs menu-col" style="left:28px">
    <li>Lorem Ipsum</li><li>Donor Ippsum</li><li>Amet sit</li><li>Non Augue Nec</li><li>Aliquam Sagitties</li><li>Neque Non Justo</li><li>Donor Ippsum</li>
  </ul>
  <ul class="abs menu-col" style="left:154px">
    <li>Lorem Ipsum</li><li>Donor Ippsum</li><li>Amet sit</li><li>Non Augue Nec</li><li>Aliquam Sagitties</li><li>Neque Non Justo</li><li>Donor Ippsum</li>
  </ul>
  <div class="abs dropdown-photo" role="img" aria-label="Modern white villa on a green lawn under blue sky"></div>
</div>

<div class="abs hide-label">Click to Hide</div>
<div class="abs search-panel">
  <div class="abs tab rent">Rent</div>
  <div class="abs tab buy">Buy</div>
  <div class="abs keyword">Keyword...</div>
  <div class="abs search-btn">
    <svg width="11" height="11" viewBox="0 0 11 11"><circle cx="4.5" cy="4.5" r="3.3" fill="none" stroke="#fff" stroke-width="1.6"/><path d="M7 7 10 10" stroke="#fff" stroke-width="1.8"/></svg>SEARCH PROPERTY
  </div>
</div>
<div class="abs hide-btn"><svg width="24" height="24" viewBox="0 0 24 24"><path d="M8 10 12 14 16 10" fill="none" stroke="#555" stroke-width="1.8"/></svg></div>

<h1 class="abs welcome">WELCOME TO LANTERNWAY HOMES</h1>
<p class="abs intro">Lorem ipsum dolor sit amet, consectetur adipiscing elit. In fermentum dolor non augue pretium egestas. Donec sem eros, tincidunt at congue ut, posuere sit amet est. Vivamus scelerisque viverra odio sit amet laoreet. Ut nec neque non justo rutrum tempor lobortis eu ante. Aliquam sagittis, nibh quis commodo auctor</p>
<div class="abs featured-label">Featured Properties</div>

<article class="abs card" style="left:183px">
  <div class="card-photo" role="img" aria-label="Balcony lounge with white flowers and sea view" style="background:linear-gradient(90deg,#c9cfd4,#8a7f74 60%,#3b2e28)"></div>
  <div class="ref">Ref. #: 29190</div>
</article>
<article class="abs card" style="left:358px">
  <div class="card-photo" role="img" aria-label="Living room with stone wall and cream sofas" style="background:linear-gradient(135deg,#9c8a72,#5e4c3b 60%,#c9bba5)"></div>
  <div class="card-over"><h3>Property Title</h3><p>3 bedrooms, 2 bathrooms</p><div class="plus">+</div></div>
  <div class="ref dark">Ref. #: 29190</div>
</article>
<article class="abs card" style="left:532px">
  <div class="card-photo" role="img" aria-label="Dining room with tall plants and dark chairs" style="background:linear-gradient(90deg,#a8ad9a,#595543 50%,#8f9a7a)"></div>
  <div class="ref">Ref. #: 29190</div>
</article>
<article class="abs card" style="left:707px">
  <div class="card-photo" role="img" aria-label="Sunlit living room with beige sofa and sea view" style="background:linear-gradient(90deg,#9fb1c2,#d8ccb2 50%,#b09a78)"></div>
  <div class="ref">Ref. #: 29190</div>
</article>

<a class="abs see-all">Click to See All</a>

<footer class="abs footer">
  <div class="footer-links"><span>Home</span><span>About</span><span>Services</span><span>For Sale</span><span>For Rent</span><span>Property 101</span><span>Contact</span></div>
  <div class="footer-call">CALL +852 5550 2468
    <span class="social-dot"></span><span class="social-dot"></span>
    <svg width="15" height="11" viewBox="0 0 15 11"><rect x=".5" y=".5" width="14" height="10" fill="none" stroke="#fff"/><path d="M.5 .5 7.5 6 14.5 .5" fill="none" stroke="#fff"/></svg>
  </div>
  <div class="footer-copy">All Right Reserved copyright © 2014</div>
</footer>
</body>
</html>
```